Cherish Every Note - Days Ring True

I need a website. I had a company doing it, and it looked very nice, but they went way up on hosting costs and said they owned the design of the site. I changed hosts to keep costs down. You can see the current design at farvalecaudio.example. They said I could use the copy and images from the current website. So you could cut and paste to speed things up. My logo and other images are on the current website. If you are unable to use I can send other digital copies.

Target Market(s)

seniors 55 and up

Number of Pages Required

4 page

Font styles to use
Sans Serif

Colors
0255a3
f78f20

Requirements
Must have
• Video testimonies that I can add without assistance. I use youtube links for the videos.
Nice to have
• The color scheme theme can be drawn from the logo, which is on the current webstie farvalecaudio.example
Should not have
• Should not have anything related to TonVo on the website.

```html
<!DOCTYPE html>
<html lang="en">
<head>
<meta charset="utf-8">
<title>Farvale Hearing Center</title>
<link rel="stylesheet" href="https://fonts.googleapis.com/css2?family=Exo+2:wght@400;500&family=Open+Sans:wght@600;700&display=swap">
<style>
  :root {
    --brand-orange: #f26a1b;
    --button-orange: #e0561c;
    --brand-blue: #0255a3;
    --nav-black: #000000;
    --divider: #ffffff;
    --subnav-peach: #ffdfa8;
    --subnav-text: #5a5a5a;
    --ink: #1c1c1c;
    --muted-icon: #9a9a9a;
    --hero-dark: #5b5753;
    --hero-mid: #8a8580;
    --hero-light: #b5afa8;
  }
  * { box-sizing: border-box; margin: 0; padding: 0; }
  html, body { width: 1200px; height: 582px; overflow: hidden; background: #ffffff; }
  body { font-family: "Open Sans", Arial, sans-serif; position: relative; }

  .main-nav { display: flex; height: 43px; background: var(--nav-black); }
  .main-nav a {
    flex: 1; display: flex; align-items: center; justify-content: center;
    color: #ffffff; text-decoration: none; font-weight: 700; font-size: 14px;
    letter-spacing: 0.2px; border-left: 2px solid var(--divider);
  }
  .main-nav a:first-child { border-left: none; }
  .main-nav a.is-active { background: var(--brand-orange); }

  .masthead { position: relative; height: 79px; }
  .brand {
    position: absolute; left: 14px; top: 16px; width: 380px;
    display: flex; align-items: center; gap: 10px;
  }
  .brand-mark { width: 30px; height: 30px; background: var(--brand-orange); flex: none; }
  .brand-name { color: var(--brand-blue); font-weight: 700; font-size: 20px; line-height: 1; }
  .brand-tagline {
    position: absolute; left: 54px; top: 54px; color: var(--brand-orange);
    font-size: 12px; font-weight: 600; letter-spacing: 0.6px;
  }

  .sub-nav {
    position: absolute; left: 400px; top: 0; width: 800px; height: 37px;
    background: var(--subnav-peach); display: flex; align-items: center; gap: 30px; padding-left: 26px;
  }
  .sub-nav a { color: var(--subnav-text); font-size: 11px; font-weight: 700; text-decoration: none; }

  .contact-bar {
    position: absolute; left: 400px; top: 37px; width: 800px; height: 42px;
    display: flex; align-items: center; justify-content: space-between; padding: 0 18px 0 10px;
  }
  .phone { display: flex; align-items: center; gap: 16px; font-family: "Exo 2", Arial, sans-serif; font-size: 25px; color: var(--ink); }
  .address { font-size: 13px; font-weight: 700; color: var(--ink); }

  .hero { position: absolute; left: 0; top: 122px; width: 1200px; height: 460px; overflow: hidden; }
  .hero-photo {
    position: absolute; inset: 0;
    background: linear-gradient(100deg, var(--hero-dark) 0%, var(--hero-mid) 40%, var(--hero-light) 70%, var(--hero-mid) 100%);
  }
  .hero-content { position: relative; text-align: center; color: #ffffff; font-family: "Exo 2", Arial, sans-serif; }
  .hero-title { padding-top: 84px; font-size: 38px; font-weight: 400; letter-spacing: 0.8px; }
  .hero-lead { margin-top: 19px; font-size: 24px; font-weight: 400; }
  .hero-button {
    display: inline-block; margin-top: 22px; width: 204px; height: 52px; line-height: 52px;
    background: var(--button-orange); border-radius: 12px; color: #ffffff;
    font-family: "Open Sans", Arial, sans-serif; font-size: 17px; font-weight: 600; text-decoration: none;
  }
</style>
</head>
<body>
  <nav class="main-nav">
    <a href="#" class="is-active">HOME</a>
    <a href="#">HEARING AIDS</a>
    <a href="#">SERVICES</a>
    <a href="#">EDUCATION</a>
    <a href="#">ABOUT US</a>
    <a href="#">CONTACT</a>
  </nav>

  <header class="masthead">
    <div class="brand">
      <span class="brand-mark"></span>
      <span class="brand-name">Farvale Hearing Center</span>
    </div>
    <span class="brand-tagline">Cherish every note</span>

    <div class="sub-nav">
      <a href="#">Welcome</a>
      <a href="#">News</a>
    </div>

    <div class="contact-bar">
      <span class="phone">
        <svg width="20" height="20" viewBox="0 0 24 24" fill="none" stroke="var(--muted-icon)" stroke-width="1.5" aria-hidden="true">
          <path d="M5 3h4l2 5-2.5 1.5a11 11 0 0 0 6 6L16 13l5 2v4a2 2 0 0 1-2 2A16 16 0 0 1 3 5a2 2 0 0 1 2-2z"/>
        </svg>
        (555) 014-2287
      </span>
      <span class="address">42 Linden Ave, Suite 8, Farvale, NC 20415</span>
    </div>
  </header>

  <section class="hero">
    <div class="hero-photo" role="img" aria-label="Photo of a grandfather and young boy playing together on a sandy beach"></div>
    <div class="hero-content">
      <h1 class="hero-title">RECAPTURE THE SOUNDS OF LIFE</h1>
      <p class="hero-lead">and the intimacy of a quiet conversation</p>
      <a href="#" class="hero-button">TAKE ACTION TODAY</a>
    </div>
  </section>
</body>
</html>
```